We need a web design for a retail food business based in Greater Western Sydney Australia called Golden Lantern Noodle Restaurant. Basically just need a simple yet easily to navigate website to browse through a menu, gallery , brief description about us, opening hours.
Menu and Gallery will be constantly updated.
Will provide own images for gallery
Updates
Menu has been uploaded and some idea on the colours I would like on the site
Some additional pictures added to see what designs you guys can come up with . Thanks again
To All Designers,
Any extra fee on top of the designs that feels need to be charged, please let me know in advance
Reason: Extending Deadline as I have yet to find a design that I would like...Thanks guys
Target Market(s)
All groups
Industry/Entity Type
Business
Requirements
Must have
- Open minded to any designs
Nice to have
- Would like slideshow behind main logo.
Preferred light coloured site yet not too playful
Should not have
- Preferably no dark colours backgrounds

```html
<!DOCTYPE html>
<html lang="en">
<head>
<meta charset="utf-8">
<title>Golden Lantern Noodle Restaurant</title>
<link rel="stylesheet" href="https://fonts.googleapis.com/css2?family=Open+Sans:ital,wght@0,400;0,600;0,700;1,600&family=Oswald:wght@400&family=Questrial&family=Noto+Serif&display=swap">
<style>
:root{
  --orange:#f7893a;
  --orange-dark:#c65a10;
  --heading-orange:#d8661a;
  --brown:#6b3d1a;
  --brown-dark:#5a2f10;
  --text-brown:#8a5a3a;
  --nav-text:#555;
  --cream:#f2efd6;
  --cream-line:#dcd8bc;
  --white:#ffffff;
  --green:#6cbf4a;
  --green-dark:#3f8a26;
}
*{margin:0;padding:0;box-sizing:border-box}
html,body{width:1200px;height:1130px;overflow:hidden;background:var(--white)}
body{position:relative;font-family:"Open Sans",sans-serif}
.abs{position:absolute}

/* header */
.site-header{left:0;top:0;width:1200px;height:96px;background:var(--white);border-bottom:1px solid #e3e3e3}
.brand{left:200px;top:26px;display:flex;align-items:center;gap:10px;font-family:"Open Sans",sans-serif;font-weight:700;font-size:24px;color:var(--brown-dark)}
.brand-mark{width:16px;height:16px;border-radius:50%;background:var(--orange)}
.main-nav{left:630px;top:42px;display:flex;gap:0}
.main-nav a{font-family:"Questrial",sans-serif;font-size:12.5px;color:var(--nav-text);text-decoration:none;text-transform:uppercase;padding:4px 10px;margin-right:14px}
.main-nav a.active{background:var(--orange);color:var(--white)}

/* hero */
.hero{left:0;top:96px;width:1200px;height:311px;background:linear-gradient(90deg,#6f5a3c 0%,#b49a6c 12%,#8a5a3a 30%,#c88a5a 50%,#e0b07a 62%,#8a6a3a 80%,#5a4a2a 100%)}
.hero-panel{left:188px;top:96px;width:330px;height:311px;background:rgba(40,25,10,.35)}
.hero-text{left:204px;top:120px;width:310px;color:var(--white)}
.offer-title{font-family:"Oswald",sans-serif;font-size:38px;line-height:1.05}
.offer-line{font-size:13.5px;font-weight:600;line-height:1.4;margin-bottom:16px}
.offer-line em{font-weight:600}
.hero-note{font-size:14px;line-height:1.25;margin-bottom:10px}
.hero-dots{left:207px;top:379px;display:flex;gap:5px}
.hero-dots span{width:11px;height:11px;border-radius:50%;background:#b8561a}
.hero-dots span.on{background:var(--white)}

/* about */
.about-band{left:0;top:407px;width:1200px;height:258px;background:linear-gradient(#fff,#f6f6f3);border-bottom:1px solid #ddd}
.about{left:205px;top:440px;width:490px}
.about h1{font-weight:400;font-size:21px;color:var(--brown);margin-bottom:14px}
.about p{font-size:12.5px;line-height:25.5px;color:var(--text-brown)}
.divider{left:712px;top:430px;width:1px;height:212px;background:#e2ddd4}
.hours{left:745px;top:440px;width:280px;color:var(--brown)}
.hours h2{font-weight:700;font-size:21px;margin-bottom:18px}
.hours dl{font-size:13px}
.hours .label{font-weight:700;margin-top:0}
.hours .row{display:flex;line-height:15px}
.hours .row span:first-child{width:158px}
.hours .gap{height:30px}

/* lower */
.lower{left:0;top:665px;width:1200px;height:392px;background:var(--cream);border-bottom:1px solid var(--cream-line)}
.col-title{font-weight:700;font-size:18.5px;color:var(--heading-orange);letter-spacing:.5px}
.thumb{width:66px;height:66px;border:3px solid var(--white);box-shadow:0 0 2px rgba(0,0,0,.25)}
.btn{height:31px;border-radius:16px;font-family:"Noto Serif",serif;font-size:13.5px;color:var(--white);display:flex;align-items:center;justify-content:center;box-shadow:0 1px 2px rgba(0,0,0,.3)}
.btn-orange{background:linear-gradient(#f49a4e,var(--orange-dark));border:1px solid #a84a0c}
.btn-green{background:linear-gradient(#8cd268,var(--green-dark));border:1px solid #3a7a22}
.menu-card{left:489px;top:738px;width:222px;height:220px;background:var(--white);border:1px solid #ddd}
.menu-preview{position:absolute;left:6px;top:6px;right:6px;bottom:6px;background:linear-gradient(#f4c8d8 0%,#fbe6ee 20%,#fafafa 24%,#eeeeee 100%)}
.map{left:789px;top:739px;width:219px;height:198px;border:3px solid var(--white);border-radius:4px;box-shadow:0 1px 3px rgba(0,0,0,.25);background:linear-gradient(160deg,#e6e4df,#d9d6cf 55%,#e3e0d8)}
.address{left:789px;top:948px;color:var(--brown-dark);font-size:11px;line-height:20px}
.address strong{font-size:13.5px;display:block;line-height:18px;margin-bottom:2px}

/* footer */
.footer-nav{left:0;top:1077px;width:1200px;display:flex;justify-content:center;gap:0}
.footer-nav a{font-family:"Questrial",sans-serif;font-size:12px;color:var(--nav-text);text-decoration:none;text-transform:uppercase;margin:0 17px}
.copyright{left:0;top:1101px;width:1200px;text-align:center;font-size:10.5px;color:var(--brown)}
</style>
</head>
<body>
<header class="abs site-header">
  <div class="abs brand"><span class="brand-mark"></span>Golden Lantern</div>
  <nav class="abs main-nav">
    <a class="active" href="#">Home</a><a href="#">About</a><a href="#">Gallery</a><a href="#">Menu</a><a href="#">Contact</a>
  </nav>
</header>

<section class="abs hero" role="img" aria-label="Slideshow photo of the restaurant dining room with bar and tables"></section>
<div class="abs hero-panel"></div>
<div class="abs hero-text">
  <div class="offer-title">Order over $22</div>
  <p class="offer-line">Receive 6 Mini Rolls or 6 Chicken Wings.</p>
  <div class="offer-title">Order over $40</div>
  <p class="offer-line">Receive any dish to the value of $10 (<em>or pay the difference excluding seafood dish</em>)</p>
  <p class="hero-note">Prices and Offers subject to change without notice.</p>
  <p class="hero-note">This menu is effective <strong>June 2012</strong></p>
</div>
<div class="abs hero-dots"><span></span><span></span><span class="on"></span><span></span><span></span><span></span></div>

<section class="abs about-band"></section>
<div class="abs about">
  <h1>About Golden Lantern Noodle Restaurant</h1>
  <p>Lorem ipsum dolor sit amet, consectetur adipisicing elit, sed do eiusmod tempor incididunt ut labore et dolore magna aliqua. Ut enim ad minim veniam, quis nostrud exercitation ullamco laboris nisi ut aliquip ex ea commodo consequat. Duis aute irure dolor in reprehenderit in voluptate velit esse cillum dolore eu fugiat nulla pariatur. Excepteur sint occaecat cupidatat non proident, sunt in culpa qui officia deserunt mollit anim id est laborum</p>
</div>
<div class="abs divider"></div>
<div class="abs hours">
  <h2>Open 7 Days</h2>
  <div style="padding-left:2px;font-size:13px">
    <div class="label">Lunch:</div>
    <div class="row"><span>Monday - Friday:</span><span>11:30am - 3:00pm</span></div>
    <div class="gap"></div>
    <div class="label">Dinner:</div>
    <div class="row" style="margin-top:2px"><span>Sun, Mon, Tue,<br>Wed &amp; Public Holidays:</span><span style="padding-top:8px">5:00pm - 9:30pm</span></div>
    <div style="height:14px"></div>
    <div class="row"><span>Thurs, Fri &amp; Sat:</span><span style="padding-top:2px">5:00pm - 10:30pm</span></div>
  </div>
</div>

<section class="abs lower"></section>
<h3 class="abs col-title" style="left:189px;top:700px">GALLERY</h3>
<div class="abs thumb" style="left:189px;top:738px;background:#9a7a3a" role="img" aria-label="Dish photo: lettuce wraps"></div>
<div class="abs thumb" style="left:266px;top:738px;background:#b8b2a0" role="img" aria-label="Dish photo: rice with greens"></div>
<div class="abs thumb" style="left:343px;top:738px;background:#c08a3a" role="img" aria-label="Dish photo: fried noodles"></div>
<div class="abs thumb" style="left:189px;top:815px;background:#a83a1a" role="img" aria-label="Dish photo: chilli stir fry"></div>
<div class="abs thumb" style="left:266px;top:815px;background:#d8502a" role="img" aria-label="Dish photo: sweet and sour chicken"></div>
<div class="abs thumb" style="left:343px;top:815px;background:#d8b88a" role="img" aria-label="Dish photo: spring rolls"></div>
<div class="abs thumb" style="left:189px;top:892px;background:#8a6a6a" role="img" aria-label="Dish photo: noodle bowl"></div>
<div class="abs thumb" style="left:266px;top:892px;background:#4a5a2a" role="img" aria-label="Dish photo: vegetables in wok"></div>
<div class="abs thumb" style="left:343px;top:892px;background:#c8c8a0" role="img" aria-label="Dish photo: dumpling soup"></div>
<a class="abs btn btn-orange" style="left:200px;top:973px;width:199px">Click here to View More</a>

<h3 class="abs col-title" style="left:489px;top:700px">MENU</h3>
<div class="abs menu-card"><div class="menu-preview" role="img" aria-label="Preview of the business lunch menu page"></div></div>
<a class="abs btn btn-green" style="left:489px;top:973px;width:220px">Click Here to Browse the Menu</a>

<h3 class="abs col-title" style="left:789px;top:700px">LOCATION</h3>
<div class="abs map" role="img" aria-label="Street map showing the restaurant location"></div>
<div class="abs address">
  <strong>Golden Lantern</strong>
  Shop 5, 28 Wattle Parade, Riverbend NSW 2760<br>
  (Turn right over Willow Creek Bridge)
</div>

<nav class="abs footer-nav">
  <a href="#">Home</a><a href="#">About</a><a href="#">Gallery</a><a href="#">Menu</a><a href="#">Contact</a>
</nav>
<p class="abs copyright">Copyright Golden Lantern 2013 / &nbsp; All Rights Reserved.</p>
</body>
</html>
```